Business Card Design Project - IT Company

CLOUD IT company working with medium to large corporate clients requires 2 sided Business Card design.

Strong, Professional and modern is what I am looking for.

The Logo JPG attached has all the colour palette options. which consist of Red and Silver on various backgrounds

Preferred option for the Back of card is either Silver Text on Red or Silver Text on Black. Though this is not concrete. Surprise me.

Logo must be prominent along with Contact details of the staff member

Tagline can be all Capitals " CLOUD MANAGED SERVICES"

I will look to provide feedback and tweaks to get the right design so it should be a fun process.

I will provide the layered files to the top few contenders.

Reason: Leaving the door open for some creativity. Don't forget this is an technology company. .

Target Market(s)

Leaders, decision makers, CEOs, CIOs,

Industry/Entity Type

Business

Requirements
Must have
• Data must have is

Company Name: Brelquist
Tagline: Cloud Managed Services

No Particular order

First Name Last name
Director
Mobile 0477 555 019
www.brelquist-example.com
First.Lastname@brelquist-example.com
Suite 7, 48 Wexmoor Lane, Sydney NSW 2000

```html
<!DOCTYPE html>
<html lang="en">
<head>
<meta charset="utf-8">
<title>Brelquist – Business Card</title>
<link href="https://fonts.googleapis.com/css2?family=Exo+2:wght@400;500;600;700&display=swap" rel="stylesheet">
<style>
  :root {
    --backdrop: #4a4a4a;
    --card-white: #f6f6f6;
    --card-black: #1c1c1c;
    --ink: #2a2a2a;
    --ink-soft: #3c3c3c;
    --brand-red: #8c1a1d;
    --band-grey: #a9a9a9;
    --silver: #c9c9c9;
    --silver-soft: #9a9a9a;
  }
  * { margin: 0; padding: 0; box-sizing: border-box; }
  html, body { width: 1200px; height: 1000px; overflow: hidden; }
  body {
    background: var(--backdrop);
    font-family: "Exo 2", Arial, sans-serif;
    position: relative;
  }
  .card {
    position: absolute;
    width: 528px;
    height: 300px;
    border-radius: 14px;
    overflow: hidden;
  }
  .card-front { left: 207px; top: 165px; background: var(--card-white); color: var(--ink); }
  .card-back { left: 472px; top: 535px; background: var(--card-black); color: var(--silver); }

  .brand { position: absolute; display: flex; align-items: center; gap: 10px; }
  .brand-mark { width: 44px; height: 44px; border-radius: 50%; flex: none; }
  .brand-name { font-size: 44px; font-weight: 700; line-height: 1; letter-spacing: -0.5px; }
  .brand-text { display: flex; flex-direction: column; align-items: flex-end; }
  .tagline { font-size: 10px; font-weight: 600; letter-spacing: 0.3px; margin-top: 2px; }

  .card-front .brand { left: 25px; top: 62px; }
  .card-front .brand-mark { background: var(--brand-red); }
  .card-front .brand-name { color: var(--ink); }
  .card-front .tagline { color: var(--ink); }

  .company-info {
    position: absolute;
    right: 248px;
    top: 176px;
    text-align: right;
    font-size: 12px;
    color: var(--ink-soft);
  }
  .company-info .web { margin-bottom: 20px; }
  .web strong { color: var(--brand-red); font-weight: 600; }
  .address { line-height: 15px; }

  .person { position: absolute; left: 300px; top: 152px; }
  .person-name { font-size: 17px; font-weight: 700; letter-spacing: 0.3px; color: var(--ink); }
  .person-role { font-size: 13px; color: var(--ink-soft); margin-bottom: 22px; }
  .contact-line { display: flex; align-items: center; gap: 7px; font-size: 11px; color: var(--ink); line-height: 17px; }
  .contact-line .phone-number { font-size: 13px; }
  .contact-icon { width: 14px; height: 12px; flex: none; }

  .bands { position: absolute; left: 0; bottom: 0; width: 528px; height: 24px; }

  .card-back .pattern-field {
    position: absolute; inset: 0;
    background: radial-gradient(ellipse at 50% 40%, #262626 0%, #1b1b1b 70%, #161616 100%);
  }
  .card-back .brand { left: 84px; top: 62px; }
  .card-back .brand-mark { background: var(--silver); }
  .card-back .brand-name { color: var(--silver); }
  .card-back .tagline { color: var(--silver); }
  .card-back .web {
    position: absolute; right: 172px; top: 256px;
    font-size: 14px; color: var(--silver-soft);
  }
  .card-back .web strong { color: var(--silver); }
</style>
</head>
<body>

<section class="card card-front">
  <div class="brand">
    <span class="brand-mark"></span>
    <div class="brand-text">
      <span class="brand-name">Brelquist</span>
      <span class="tagline">CLOUD MANAGED SERVICES</span>
    </div>
  </div>

  <div class="company-info">
    <p class="web">www.<strong>brelquist-example</strong>.com</p>
    <p class="address">Suite 7, 48 Wexmoor Lane<br>Sydney NSW 2000</p>
  </div>

  <div class="person">
    <p class="person-name">DANA CORVELL</p>
    <p class="person-role">Director</p>
    <p class="contact-line">
      <svg class="contact-icon" viewBox="0 0 14 12" aria-hidden="true"><rect x="4" y="0.5" width="6" height="11" rx="1.2" fill="none" stroke="#8c1a1d" stroke-width="1.4"/><rect x="6" y="9" width="2" height="1.2" fill="#8c1a1d"/></svg>
      <span class="phone-number">0477 555 019</span>
    </p>
    <p class="contact-line">
      <svg class="contact-icon" viewBox="0 0 14 12" aria-hidden="true"><rect x="0.5" y="2" width="13" height="9" fill="#8c1a1d"/><path d="M0.5 2 L7 7 L13.5 2" fill="none" stroke="#f6f6f6" stroke-width="1.2"/></svg>
      <span>dana.corvell@brelquist-example.com</span>
    </p>
  </div>

  <svg class="bands" viewBox="0 0 528 24" aria-hidden="true">
    <polygon points="0,12 292,12 284,24 0,24" fill="var(--band-grey)"/>
    <polygon points="300,2 528,2 528,24 290,24" fill="var(--brand-red)"/>
  </svg>
</section>

<section class="card card-back">
  <div class="pattern-field" role="img" aria-label="Faint repeating brand-symbol pattern on black"></div>
  <div class="brand">
    <span class="brand-mark"></span>
    <div class="brand-text">
      <span class="brand-name">Brelquist</span>
      <span class="tagline">CLOUD MANAGED SERVICES</span>
    </div>
  </div>
  <p class="web">www.<strong>brelquist-example</strong>.com</p>
</section>

</body>
</html>
```